Business Card Design Project

Small privately owned salon.

Industry/Entity Type

Business

Contact Information for Business Card

Hair salon.i would like my logo to be my name , Marisol Denby. Address and phone can go on the front or back. The back will be where I write their appt.
address-362 Thistledown lane York, Pa. 17488
Phone- 717-555-0148

```html
<!DOCTYPE html>
<html lang="en">
<head>
<meta charset="utf-8">
<title>Hair Creations by Marisol Denby — Business Card</title>
<link rel="stylesheet" href="https://fonts.googleapis.com/css2?family=Josefin+Sans:wght@300;400&family=Questrial&display=swap">
<style>
  :root {
    --salon-red: #e33d32;
    --salon-red-deep: #d2343a;
    --strand-teal: #3c8e87;
    --strand-gold: #efcf5c;
    --strand-magenta: #c51f4d;
    --strand-plum: #3f1a30;
    --band-plum: rgba(70, 22, 48, 0.93);
    --type-white: #ffffff;
  }

  * { margin: 0; padding: 0; box-sizing: border-box; }

  html, body {
    width: 1200px;
    height: 720px;
    overflow: hidden;
    background: #ffffff;
  }

  .business-card {
    position: relative;
    width: 1200px;
    height: 720px;
    overflow: hidden;
    background: var(--salon-red);
  }

  .hair-artwork {
    position: absolute;
    inset: 0;
    background:
      radial-gradient(ellipse 240px 200px at 590px 270px, var(--salon-red) 0%, var(--salon-red) 45%, rgba(227, 61, 50, 0) 100%),
      radial-gradient(ellipse 300px 240px at 250px 170px, rgba(239, 207, 92, 0.85) 0%, rgba(239, 207, 92, 0) 75%),
      radial-gradient(ellipse 260px 200px at 780px 130px, rgba(239, 207, 92, 0.75) 0%, rgba(239, 207, 92, 0) 75%),
      radial-gradient(ellipse 300px 230px at 930px 260px, rgba(60, 142, 135, 0.85) 0%, rgba(60, 142, 135, 0) 75%),
      radial-gradient(ellipse 260px 220px at 140px 340px, rgba(60, 142, 135, 0.8) 0%, rgba(60, 142, 135, 0) 75%),
      radial-gradient(ellipse 280px 220px at 1110px 120px, rgba(197, 31, 77, 0.8) 0%, rgba(197, 31, 77, 0) 75%),
      radial-gradient(ellipse 260px 200px at 430px 80px, rgba(197, 31, 77, 0.8) 0%, rgba(197, 31, 77, 0) 75%),
      radial-gradient(ellipse 300px 160px at 200px 660px, rgba(60, 142, 135, 0.8) 0%, rgba(60, 142, 135, 0) 75%),
      radial-gradient(ellipse 320px 150px at 620px 680px, rgba(239, 207, 92, 0.75) 0%, rgba(239, 207, 92, 0) 75%),
      radial-gradient(ellipse 300px 160px at 1020px 660px, rgba(197, 31, 77, 0.8) 0%, rgba(197, 31, 77, 0) 75%),
      linear-gradient(180deg, rgba(63, 26, 48, 0.45) 0%, rgba(63, 26, 48, 0) 30%),
      linear-gradient(160deg, var(--salon-red) 0%, var(--salon-red-deep) 100%);
  }

  .name-band {
    position: absolute;
    left: 0;
    top: 403px;
    width: 1200px;
    height: 194px;
    background: var(--band-plum);
  }

  .tagline {
    position: absolute;
    left: 158px;
    top: 428px;
    font-family: "Questrial", sans-serif;
    font-size: 38px;
    font-weight: 400;
    color: var(--type-white);
    letter-spacing: 0.5px;
    line-height: 1;
  }

  .salon-name {
    position: absolute;
    left: 88px;
    top: 478px;
    font-family: "Josefin Sans", sans-serif;
    font-size: 112px;
    font-weight: 300;
    color: var(--type-white);
    letter-spacing: 6px;
    line-height: 1;
    text-transform: uppercase;
    white-space: nowrap;
  }
</style>
</head>
<body>
  <main class="business-card">
    <div class="hair-artwork" role="img" aria-label="Illustration of long flowing hair in strands of gold, teal, magenta and plum sweeping across a red background"></div>

    <div class="name-band"></div>
    <p class="tagline">hair creations by</p>
    <h1 class="salon-name">Marisol Denby</h1>
  </main>
</body>
</html>
```